Bref créative
Stationery for interior design business
Venmark Interiors, LLC
Simple
Cleo Venmark
Interior Designer
No address on card or stationery
cleo@venmarkinteriors.example
venmarkinteriors.example
Please also include my blog address on the front of the card: cleovenmark.example
Open for design suggestions, but I'd like either the entire logo or only the sphere to appear on the back

```html
<!DOCTYPE html>
<html lang="en">
<head>
<meta charset="utf-8">
<title>Venmark Interiors — Stationery</title>
<link rel="stylesheet" href="https://fonts.googleapis.com/css2?family=Cormorant+Garamond:wght@600&family=Open+Sans:wght@400;600&display=swap">
<style>
  :root {
    --bg: #eceef1;
    --paper: #ffffff;
    --brand-blue: #3b3fb2;
    --brand-blue-light: #5a5ed0;
    --swoosh-grey: #8a8a8e;
    --ink: #3a3a3f;
    --ink-soft: #6b6b72;
    --faint: #e6e7ec;
  }
  * { box-sizing: border-box; margin: 0; padding: 0; }
  html, body { width: 1200px; height: 936px; overflow: hidden; }
  body {
    position: relative;
    background: var(--bg);
    font-family: "Open Sans", Arial, sans-serif;
    color: var(--ink);
  }
  .sheet {
    position: absolute;
    background: var(--paper);
    box-shadow: 0 2px 6px rgba(0,0,0,.12);
    overflow: hidden;
  }
  .wave { position: absolute; left: 0; bottom: 0; width: 100%; display: block; }

  .brand {
    display: flex; align-items: center; gap: .35em;
    font-family: "Cormorant Garamond", Georgia, serif;
    font-weight: 600;
    color: var(--ink);
    white-space: nowrap;
  }
  .brand-dot { width: 1.1em; height: 1.1em; border-radius: 50%; background: var(--brand-blue); flex: none; }

  /* Letterhead */
  .letterhead { left: 183px; top: 63px; width: 388px; height: 551px; }
  .letterhead .brand { position: absolute; left: 24px; top: 28px; font-size: 19px; }
  .contact-list { position: absolute; left: 272px; top: 20px; list-style: none; font-size: 6.5px; line-height: 11px; color: var(--ink-soft); }
  .contact-list li { display: flex; align-items: center; gap: 4px; }
  .contact-list li::before { content: ""; width: 5px; height: 5px; border-radius: 50%; background: var(--brand-blue); }
  .faint-mark { position: absolute; left: 50%; top: 230px; transform: translateX(-50%); display: flex; flex-direction: column; align-items: center; gap: 8px; }
  .faint-mark .disc { width: 110px; height: 110px; border-radius: 50%; background: var(--faint); }
  .faint-mark span { font-family: "Cormorant Garamond", Georgia, serif; font-weight: 600; font-size: 20px; color: var(--faint); }

  /* Cover sheet */
  .cover { left: 634px; top: 38px; width: 462px; height: 578px; }
  .cover .brand { position: absolute; left: 50%; top: 218px; transform: translateX(-50%); font-size: 44px; }

  /* Business cards */
  .card-front { left: 43px; top: 660px; width: 193px; height: 102px; }
  .card-front .brand { position: absolute; left: 12px; top: 14px; font-size: 12px; }
  .card-person { position: absolute; left: 12px; top: 46px; font-size: 5.5px; line-height: 8px; }
  .card-person strong { font-weight: 600; display: block; }
  .card-front .contact-list { left: 100px; top: 46px; font-size: 5px; line-height: 8px; }
  .card-front .contact-list li::before { width: 4px; height: 4px; }

  .card-back { left: 43px; top: 781px; width: 193px; height: 112px; background: var(--brand-blue); }
  .card-back .disc { position: absolute; left: 50%; top: 26px; transform: translateX(-50%); width: 44px; height: 44px; border-radius: 50%; background: var(--paper); }
  .card-back .site { position: absolute; width: 100%; top: 84px; text-align: center; font-size: 6px; letter-spacing: .5px; color: var(--paper); }

  /* Envelopes */
  .envelope-front { left: 266px; top: 667px; width: 432px; height: 213px; }
  .envelope-front .brand { position: absolute; left: 14px; top: 18px; font-size: 17px; }

  .envelope-back { left: 736px; top: 667px; width: 421px; height: 221px; }
  .envelope-back .flap { position: absolute; left: 0; top: 0; width: 100%; height: 110px; display: block; }
  .envelope-back .site { position: absolute; width: 100%; top: 40px; text-align: center; font-size: 9px; letter-spacing: 2.5px; color: var(--paper); }
</style>
</head>
<body>

  <!-- Letterhead -->
  <section class="sheet letterhead">
    <div class="brand"><span class="brand-dot"></span>Venmark Interiors</div>
    <ul class="contact-list">
      <li>(555) 014-2290</li>
      <li>cleo@venmarkinteriors.example</li>
      <li>venmarkinteriors.example</li>
      <li>cleovenmark.example</li>
    </ul>
    <div class="faint-mark"><div class="disc"></div><span>Venmark Interiors</span></div>
    <svg class="wave" viewBox="0 0 388 50" preserveAspectRatio="none" height="50">
      <path d="M0 20 C120 2 260 2 388 14 L388 18 C260 8 120 10 0 26 Z" fill="var(--swoosh-grey)"/>
      <path d="M0 32 C120 14 250 10 388 22 L388 50 L0 50 Z" fill="var(--brand-blue)"/>
    </svg>
  </section>

  <!-- Cover sheet -->
  <section class="sheet cover">
    <div class="brand"><span class="brand-dot"></span>Venmark Interiors</div>
    <svg class="wave" viewBox="0 0 462 58" preserveAspectRatio="none" height="58">
      <path d="M0 16 C150 4 310 10 462 26 L462 30 C310 16 150 12 0 22 Z" fill="var(--swoosh-grey)"/>
      <path d="M0 28 C150 18 310 22 462 38 L462 58 L0 58 Z" fill="var(--brand-blue)"/>
    </svg>
  </section>

  <!-- Business card front -->
  <section class="sheet card-front">
    <div class="brand"><span class="brand-dot"></span>Venmark Interiors</div>
    <div class="card-person"><strong>Cleo Venmark</strong>Interior Designer</div>
    <ul class="contact-list">
      <li>(555) 014-2290</li>
      <li>cleo@venmarkinteriors.example</li>
      <li>venmarkinteriors.example</li>
      <li>cleovenmark.example</li>
    </ul>
    <svg class="wave" viewBox="0 0 193 14" preserveAspectRatio="none" height="14">
      <path d="M0 6 C60 0 130 2 193 8 L193 14 L0 14 Z" fill="var(--brand-blue)"/>
    </svg>
  </section>

  <!-- Business card back -->
  <section class="sheet card-back">
    <div class="disc"></div>
    <p class="site">www.venmarkinteriors.example</p>
  </section>

  <!-- Envelope front -->
  <section class="sheet envelope-front">
    <div class="brand"><span class="brand-dot"></span>Venmark Interiors</div>
    <svg class="wave" viewBox="0 0 432 60" preserveAspectRatio="none" height="60">
      <path d="M0 18 C140 0 300 4 432 20 L432 24 C300 10 140 8 0 26 Z" fill="var(--swoosh-grey)"/>
      <path d="M0 34 C140 16 300 18 432 34 L432 60 L0 60 Z" fill="var(--brand-blue)"/>
    </svg>
  </section>

  <!-- Envelope back -->
  <section class="sheet envelope-back">
    <svg class="flap" viewBox="0 0 421 110" preserveAspectRatio="none">
      <path d="M0 0 L421 0 L421 70 L210 110 L0 70 Z" fill="var(--brand-blue)"/>
    </svg>
    <p class="site">www.venmarkinteriors.example</p>
  </section>

</body>
</html>
```